Cool modern, tech Business card design

Looking for a new business card design for our Managed IT Services company. We would like 2 sides, with the logo one one side horizontally and then the information on the back in either vertical or horizontal. We want our colors from the logo incorporated but also would like to see the color gray in there as well.

Target Market(s)

IT, Information Technology, Tech, Service

Industry/Entity Type

It Service

Contact Information for Business Card

Pavel Lind
Managing Partner
(P)742-318-6650 ext xxx
(F)742-318-6651
www.qelvantrixo.com

Font styles to use
Sans Serif

Colors
959595
000000
ec1f27

Requirements
Must have
• Logo on one side with some nice design or pattern
• Information on back in either vertical or horizontal format
Nice to have
• For it to look cool, tech, modern, stand out.

```html
<!DOCTYPE html>
<html lang="en">
<head>
<meta charset="utf-8">
<title>Qelvantrixo Business Card</title>
<link rel="stylesheet" href="https://fonts.googleapis.com/css2?family=Lato:wght@400;700&display=swap">
<style>
  :root {
    --brand-red: #d0182f;
    --ink: #1b1b1b;
    --gray: #959595;
    --paper: #fbfbfb;
    --backdrop: #2a2a2a;
    --band-dark: #231f20;
  }
  * { box-sizing: border-box; margin: 0; padding: 0; }
  html, body {
    width: 1200px;
    height: 900px;
    overflow: hidden;
    background: var(--backdrop);
    font-family: "Lato", sans-serif;
  }
  .canvas {
    position: relative;
    width: 1200px;
    height: 900px;
  }
  .card {
    position: absolute;
    width: 560px;
    height: 320px;
    overflow: hidden;
    box-shadow: 0 18px 40px rgba(0,0,0,0.55);
  }
  .card--front {
    left: 60px;
    top: 90px;
    background: var(--brand-red);
    display: flex;
    align-items: center;
    justify-content: center;
  }
  .card--back {
    left: 580px;
    top: 490px;
    background: var(--paper);
  }
  .wordmark {
    display: flex;
    align-items: center;
    gap: 14px;
    font-family: "Lato", sans-serif;
    font-weight: 400;
    letter-spacing: 1px;
  }
  .wordmark__square {
    display: block;
    border-radius: 4px;
  }
  .card--front .wordmark { color: #ffffff; font-size: 54px; }
  .card--front .wordmark__square { width: 26px; height: 26px; background: #ffffff; }

  .card--back .wordmark {
    position: absolute;
    right: 36px;
    top: 40px;
    color: var(--ink);
    font-size: 34px;
    gap: 10px;
  }
  .card--back .wordmark__square { width: 16px; height: 16px; background: var(--brand-red); }

  .contact {
    position: absolute;
    left: 34px;
    bottom: 52px;
    color: var(--ink);
  }
  .contact__name {
    font-size: 19px;
    font-weight: 400;
    color: var(--brand-red);
    line-height: 1.1;
  }
  .contact__name strong { color: var(--ink); font-weight: 700; }
  .contact__title {
    font-size: 12px;
    color: #333;
    margin-top: 2px;
  }
  .contact__web {
    font-size: 13px;
    font-weight: 700;
    margin-top: 14px;
    margin-bottom: 12px;
  }
  .contact__list { list-style: none; }
  .contact__item {
    display: flex;
    align-items: center;
    gap: 8px;
    font-size: 12.5px;
    line-height: 1.55;
  }
  .contact__icon { width: 13px; height: 13px; fill: var(--brand-red); flex: none; }

  .edge-band {
    position: absolute;
    left: 0;
    bottom: 0;
    width: 100%;
    height: 12px;
    display: flex;
  }
  .edge-band__red { flex: 1; background: var(--brand-red); }
  .edge-band__dark { width: 130px; background: var(--band-dark); }
</style>
</head>
<body>
<main class="canvas">
  <section class="card card--front" aria-label="Card front">
    <div class="wordmark">
      <span>qelvantrixo</span>
      <span class="wordmark__square" aria-hidden="true"></span>
    </div>
  </section>

  <section class="card card--back" aria-label="Card back">
    <div class="wordmark">
      <span>qelvantrixo</span>
      <span class="wordmark__square" aria-hidden="true"></span>
    </div>

    <div class="contact">
      <p class="contact__name">Pavel <strong>Lind</strong></p>
      <p class="contact__title">Managing Partner</p>
      <p class="contact__web">www.qelvantrixo.com</p>
      <ul class="contact__list">
        <li class="contact__item">
          <svg class="contact__icon" viewBox="0 0 16 16" aria-hidden="true"><path d="M3.5 1.5l2.5 2.6-1.4 1.8a9 9 0 0 0 5.5 5.5l1.8-1.4 2.6 2.5-1.6 2A12.5 12.5 0 0 1 1.5 3.1z"/></svg>
          742-318-6650
        </li>
        <li class="contact__item">
          <svg class="contact__icon" viewBox="0 0 16 16" aria-hidden="true"><path d="M4 1h8v4H4zM1 6h14v7h-3v2H4v-2H1zm4 5v3h6v-3z"/></svg>
          742-318-6651
        </li>
        <li class="contact__item">
          <svg class="contact__icon" viewBox="0 0 16 16" aria-hidden="true"><path d="M1 3h14v10H1zm1.5 1.4V5l5.5 4 5.5-4v-.6z"/></svg>
          pavel@qelvantrixo.com
        </li>
      </ul>
    </div>

    <div class="edge-band" aria-hidden="true">
      <span class="edge-band__red"></span>
      <span class="edge-band__dark"></span>
    </div>
  </section>
</main>
</body>
</html>
```